Stationary (Business Cards, envelopes, cover letters, etc) for HARBOR LANTERN PARTNERS
The Harbor Lantern Partners
Stationary (Business Cards, envelopes, cover letters, etc) for HARBOR LANTERN PARTNERS - Business Opportunities
Creative Brief
Professional
Rodrigo Velasco Brennan
Av. Ignacio Marroquín 718 B Col. Los Pinos Altos México DF CP 01482 México
rvelasco@hlp-example.mx
www.hlp-example.mx
First impressions have high impact, so in terms of the business card, it has to be something that's out of the box. The card is used to present ourselves to another party or prospect, but it also has to have a high impact message, either by an image or a phrase that comes attached in the back side. It could be some key points of a preview success case. So the back side has to have a marketing application. It has to be a card that will stand out, so much that it will be shown and passed around. In design and in materials (maybe???), although win the materials it will have a high impact on the costs of production. It has to be standard size, so it fits in every wallet thus avoiding on being thrown somewhere.
Concepts
Business Card and Stationary Project for a multifaceted corporation
Stationary for holding company
Business cards for RFTV - Investimentos e Administrações
mitiha mitiha
GREAT NEWS! WE'VE EXTENDED TO THIS FRIDAY! KEEP UP THE GREAT WORK!!!
Hi designers! GREAT JOB! We are want to decide today (our time) the winner. Please if you have any questions, let us know. Try to show as much applications as possible, i.e. we're now in a digital world so some digital applications we'll be considered for higher points. Have seen proposals in blue and gray (predominant colors and mixed), but none in orange. Let's see some! *Don't use curved lines in your design proposals. THANKS!
Hi, first of all I want to thank each and every one of you for accepting in working on our project. GREAT DESIGNS !!!!! Something we don't want is the lines that make a "curve" to separate content. I've seen a lot of those in the market and we want to be ORIGINAL. As I said in the brief, we want our cards to be saved as something awsome, and to be shown to other people. Material: sent your proposals of other materials, however if you can also send the specificatiosn of that material so we can see the cost of printing in them. Remember that it's not only the business cards but the stationary. KEEP UP THE GREAT JOB! CREATE DESIGN!

```html
<!DOCTYPE html>
<html lang="en">
<head>
<meta charset="utf-8">
<title>Harbor Lantern Partners — Business Cards</title>
<link href="https://fonts.googleapis.com/css2?family=Cinzel:wght@400;600&display=swap" rel="stylesheet">
<style>
  :root {
    --backdrop: #8c8c8c;
    --card-black: #0d0d0d;
    --card-white: #f7f7f7;
    --ink-white: #f2f2f2;
    --ink-dark: #1c1c1c;
    --accent-blue: #2f9fe0;
    --accent-orange: #f08a24;
    --rule: #9a9a9a;
  }
  * { box-sizing: border-box; margin: 0; padding: 0; }
  html, body { width: 1200px; height: 908px; overflow: hidden; }
  body {
    background: var(--backdrop);
    font-family: "Cinzel", "Times New Roman", serif;
    position: relative;
  }
  .card {
    position: absolute;
    width: 540px;
    height: 308px;
    border-radius: 26px;
    overflow: hidden;
  }
  .card-front { left: 80px; top: 120px; background: var(--card-black); }
  .card-back { left: 580px; top: 480px; background: var(--card-white); }

  /* front */
  .front-mark {
    position: absolute; right: 40px; top: 40px;
    display: flex; align-items: center; gap: 14px;
    color: var(--ink-white); font-size: 22px; font-weight: 600; letter-spacing: 2px;
  }
  .mark-square { width: 34px; height: 34px; background: var(--accent-orange); }

  .wordmark { position: absolute; text-align: center; }
  .wordmark .the { display: block; font-size: 10px; letter-spacing: 3px; }
  .wordmark .name {
    display: block; font-size: 17px; letter-spacing: 1.5px;
    border-top: 1px solid var(--rule); border-bottom: 1px solid var(--rule);
    padding: 4px 2px; margin-top: 3px;
  }
  .card-front .wordmark { left: 40px; bottom: 44px; color: var(--ink-white); }
  .card-back .wordmark { left: 22px; top: 160px; color: var(--ink-dark); width: 220px; }
  .card-back .wordmark .name { font-size: 12.5px; letter-spacing: 0.6px; }
  .back-square { width: 22px; height: 22px; background: var(--accent-blue); margin: 0 auto 8px; }

  /* back contact panel */
  .contact-panel {
    position: absolute; right: 0; top: 0; bottom: 0; width: 278px;
    background: var(--card-black); border-radius: 22px 0 0 0;
    color: var(--ink-white); padding: 30px 20px 0 24px;
  }
  .contact-name { color: var(--accent-blue); font-size: 13px; letter-spacing: 1px; margin-bottom: 26px; }
  .contact-list { list-style: none; font-size: 10px; line-height: 1.45; }
  .contact-list li { display: flex; gap: 8px; align-items: flex-start; margin-bottom: 6px; }
  .icon { flex: 0 0 13px; width: 13px; height: 13px; margin-top: 1px; }
  .icon circle { fill: var(--accent-orange); }
  .icon path { fill: none; stroke: var(--card-black); stroke-width: 1.3; stroke-linecap: round; stroke-linejoin: round; }
</style>
</head>
<body>
  <section class="card card-front" aria-label="Business card front">
    <div class="front-mark"><span class="mark-square"></span>HARBOR LANTERN PARTNERS</div>
    <div class="wordmark">
      <span class="the">THE</span>
      <span class="name">HARBOR LANTERN PARTNERS</span>
    </div>
  </section>

  <section class="card card-back" aria-label="Business card back">
    <div class="wordmark">
      <div class="back-square"></div>
      <span class="the">THE</span>
      <span class="name">HARBOR LANTERN PARTNERS</span>
    </div>
    <div class="contact-panel">
      <p class="contact-name">RODRIGO VELASCO BRENNAN</p>
      <ul class="contact-list">
        <li>
          <svg class="icon" viewBox="0 0 13 13"><circle cx="6.5" cy="6.5" r="6.5"/><path d="M6.5 10 L4 6 A2.6 2.6 0 1 1 9 6 Z"/></svg>
          <span>Av. Ignacio Marroquín 718 B<br>Col. Los Pinos Altos<br>México DF CP 01482 México</span>
        </li>
        <li>
          <svg class="icon" viewBox="0 0 13 13"><circle cx="6.5" cy="6.5" r="6.5"/><path d="M4 3.5 L5.5 3.5 L6 5.5 L5 6.2 Q6 8 7 8.3 L7.8 7.3 L9.5 7.8 L9.5 9.3 Q6 9.5 4 6 Z"/></svg>
          <span>+52 55 0148 2270</span>
        </li>
        <li>
          <svg class="icon" viewBox="0 0 13 13"><circle cx="6.5" cy="6.5" r="6.5"/><path d="M4.6 3 H8.4 V10 H4.6 Z M6 8.7 H7"/></svg>
          <span>+52 1 55 8193 0046</span>
        </li>
        <li>
          <svg class="icon" viewBox="0 0 13 13"><circle cx="6.5" cy="6.5" r="6.5"/><path d="M3.3 4.3 H9.7 V8.8 H3.3 Z M3.3 4.3 L6.5 6.8 L9.7 4.3"/></svg>
          <span>rvelasco@hlp-example.mx</span>
        </li>
        <li>
          <svg class="icon" viewBox="0 0 13 13"><circle cx="6.5" cy="6.5" r="6.5"/><path d="M6.5 3 A3.5 3.5 0 1 0 6.5 10 A3.5 3.5 0 1 0 6.5 3 M3 6.5 H10 M6.5 3 Q4.8 6.5 6.5 10 M6.5 3 Q8.2 6.5 6.5 10"/></svg>
          <span>www.hlp-example.mx</span>
        </li>
      </ul>
    </div>
  </section>
</body>
</html>
```